Young Accounting firm needing a captivating business card

We need a business card design that forces the person to look at the card because its either gold foil, plastic, or lettering pop up etc. We already have a logo with a specific gold color and we need to make it pop. We are an accounting firm. I need the words" accounting, payroll, licenses, audits, taxes" somewhere on the business card so as to describe what we do- preferably on the side where the logo is at.

Industry/Entity Type

Accounting

Contact Information for Business Card

Address 48276 9th Ave S Ste 305, Federal Way, WA 98117
Business Phone (360)418-2096
Fax (360)418-2157
Office Cell Phone (360)586-7319

Font styles to use
Serif

Colors
85abd2

Requirements
Must have
• It should state
• "Accounting" "Taxes" "Audits" "Licenses" "Payroll"
Nice to have
• Matte with gold foil, different textures, With Either a textured ivory background or gray blue slate background
Should not have
• colorful colors

```html
<!DOCTYPE html>
<html lang="en">
<head>
<meta charset="utf-8">
<title>Kestrel Ledger business card</title>
<link href="https://fonts.googleapis.com/css2?family=Open+Sans:ital,wght@0,400;0,600;0,700;0,800;1,400&display=swap" rel="stylesheet">
<style>
  :root {
    --gold: #b0912c;
    --gold-deep: #9a7d22;
    --gold-light: #c4a43a;
    --navy: #1f2433;
    --ink: #2b2f3a;
    --paper: #ffffff;
    --paper-shade: #eceef0;
    --backdrop: #e4e5e8;
  }
  * { margin: 0; padding: 0; box-sizing: border-box; }
  html, body {
    width: 1200px; height: 800px; overflow: hidden;
    background: var(--backdrop);
    font-family: "Open Sans", Arial, sans-serif;
  }
  .canvas {
    position: relative; width: 1200px; height: 800px;
    display: flex; align-items: center; justify-content: center; gap: 40px;
  }
  .card {
    position: relative; width: 540px; height: 310px; overflow: hidden;
    box-shadow: 0 12px 30px rgba(0,0,0,.18);
  }
  /* front */
  .card-front { background: linear-gradient(135deg, var(--paper) 55%, var(--paper-shade)); }
  .card-front .shapes { position: absolute; inset: 0; }
  .brand-front {
    position: absolute; left: 40px; top: 138px;
    display: flex; align-items: center; gap: 10px;
  }
  .brand-mark { width: 26px; height: 26px; background: var(--gold); border-radius: 3px; }
  .brand-name { font-size: 30px; font-weight: 600; color: var(--gold); letter-spacing: -0.5px; }
  .contact {
    position: absolute; left: 285px; top: 40px;
    border-left: 1px solid var(--gold); padding-left: 14px; height: 170px;
  }
  .person-name { font-size: 22px; font-weight: 800; color: var(--navy); line-height: 1.1; }
  .person-role { font-size: 12px; font-style: italic; color: var(--gold); margin-top: 2px; }
  .address { font-size: 10.5px; color: var(--ink); line-height: 1.35; margin-top: 4px; }
  .contact-list { list-style: none; margin-top: 16px; }
  .contact-list li {
    display: flex; align-items: center; gap: 8px;
    font-size: 11.5px; color: var(--ink); margin-bottom: 7px;
  }
  .contact-list svg { width: 13px; height: 13px; flex: none; }
  .services {
    font-size: 11px; font-weight: 700; letter-spacing: .3px; text-transform: uppercase;
    white-space: nowrap;
  }
  .services-front { position: absolute; left: 215px; top: 277px; color: var(--navy); }
  /* back */
  .card-back {
    background: linear-gradient(160deg, var(--gold-light), var(--gold) 45%, var(--gold-deep));
  }
  .back-glow {
    position: absolute; right: -40px; top: -30px; width: 300px; height: 300px;
    border-radius: 50%; background: rgba(255,255,255,.06);
  }
  .back-content {
    position: absolute; inset: 0; display: flex; flex-direction: column;
    align-items: center; justify-content: center; gap: 14px;
  }
  .brand-back { display: flex; align-items: center; gap: 12px; }
  .brand-back .brand-mark { background: var(--navy); width: 34px; height: 34px; }
  .brand-back .brand-name { color: var(--navy); font-size: 38px; }
  .services-back { color: var(--navy); font-size: 12.5px; }
</style>
</head>
<body>
<main class="canvas">
  <section class="card card-front" aria-label="Business card front">
    <svg class="shapes" viewBox="0 0 540 310" preserveAspectRatio="none" aria-hidden="true">
      <polygon points="0,296 205,262 185,310 0,310" fill="var(--navy)"/>
      <polygon points="200,255 540,255 540,310 176,310" fill="var(--gold)"/>
    </svg>
    <div class="brand-front">
      <span class="brand-mark"></span>
      <span class="brand-name">Kestrel Ledger</span>
    </div>
    <div class="contact">
      <h1 class="person-name">YOUR NAME</h1>
      <p class="person-role">Manager</p>
      <p class="address">48276 9th Ave S Ste 305, Federal Way,<br>WA 98117</p>
      <ul class="contact-list">
        <li>
          <svg viewBox="0 0 24 24"><path fill="var(--gold)" d="M6.6 10.8a15 15 0 0 0 6.6 6.6l2.2-2.2c.3-.3.7-.4 1-.2 1.1.4 2.3.6 3.6.6.6 0 1 .4 1 1V20c0 .6-.4 1-1 1C10.6 21 3 13.4 3 4c0-.6.4-1 1-1h3.5c.6 0 1 .4 1 1 0 1.3.2 2.5.6 3.6.1.3 0 .7-.2 1z"/></svg>
          <span>: (360)418-2096</span>
        </li>
        <li>
          <svg viewBox="0 0 24 24"><rect x="6" y="2" width="12" height="20" rx="2" fill="none" stroke="var(--gold)" stroke-width="2.2"/><circle cx="12" cy="18" r="1.2" fill="var(--gold)"/></svg>
          <span>: (360)586-7319</span>
        </li>
        <li>
          <svg viewBox="0 0 24 24"><rect x="2" y="5" width="20" height="14" rx="1.5" fill="var(--gold)"/><path d="M3 6l9 7 9-7" fill="none" stroke="var(--paper)" stroke-width="1.6"/></svg>
          <span>: youremail@kestrelledger.com</span>
        </li>
      </ul>
    </div>
    <p class="services services-front">Accounting • Payroll • Licenses • Audits • Taxes</p>
  </section>

  <section class="card card-back" aria-label="Business card back">
    <div class="back-glow"></div>
    <div class="back-content">
      <div class="brand-back">
        <span class="brand-mark"></span>
        <span class="brand-name">Kestrel Ledger</span>
      </div>
      <p class="services services-back">Accounting • Payroll • Licenses • Audits • Taxes</p>
    </div>
  </section>
</main>
</body>
</html>
```